organic and vegetable shampoo for dogs

we would like to improve the label of an already existing product which will be part of a range of 5 products. we therefore need labels that are identical but modular in relation to the product.
we have developed a range of vegetable and organic products for dog owners.
We prefer that there are no pictures of dogs, only a drawing or symbol that informs the use of the product on dogs.
It is important to highlight the "vegetable" side;
Free of petro-chemical products, paraben-free, dye-free, synthetic fragrance-free, silicone-free.
we can also accept another typo for the name VERA-MOLUND
The bottle is white and round the height of the label is 115mm and the length 147mm; the visible part is 50mm wide.
there are currently 4 different shampoos:
mild shampoo, shampoo for sensitive skin,
color-enhancing shampoos, anti-hair loss shampoo.
A description in French and in English must be provided.

```html
<!DOCTYPE html>
<html lang="fr">
<head>
<meta charset="utf-8">
<title>Vera-Molund – Shampooing Doux</title>
<link href="https://fonts.googleapis.com/css2?family=Heebo:wght@400;500;700;800&family=Oswald:wght@600&display=swap" rel="stylesheet">
<style>
  :root {
    --red: #e30613;
    --accent-red: #e2123a;
    --text-grey: #555555;
    --soft-grey: #6b6b6b;
    --leaf-grey: #ececec;
    --green: #5a7a2c;
    --trim-blue: #29a3dc;
    --white: #ffffff;
  }
  * { margin: 0; padding: 0; box-sizing: border-box; }
  html, body { width: 1200px; height: 1200px; overflow: hidden; background: var(--white); }
  body { position: relative; font-family: "Heebo", sans-serif; color: var(--text-grey); }

  .label {
    position: absolute; left: 167px; top: 47px;
    width: 866px; height: 1106px;
    border: 1.5px solid var(--trim-blue);
    background: var(--white);
    overflow: hidden;
  }
  .leaf-backdrop {
    position: absolute; left: 100px; top: 20px; width: 740px; height: 940px;
    background: radial-gradient(ellipse at 55% 50%, rgba(236,236,236,0.9) 0%, rgba(236,236,236,0.45) 45%, rgba(255,255,255,0) 72%);
  }
  .centered { position: absolute; left: 0; width: 100%; text-align: center; }

  .brand {
    top: 28px; font-weight: 800; font-size: 46px; letter-spacing: 1px;
    color: #111111; line-height: 1;
  }
  .brand-rule { position: absolute; left: 0; top: 107px; width: 100%; height: 9px; background: var(--red); }

  .paw-icon { position: absolute; left: 378px; top: 155px; width: 110px; height: 110px; }

  .title-fr { top: 287px; font-weight: 700; font-size: 33px; letter-spacing: 0.5px; line-height: 1; }
  .title-accent { font-family: "Oswald", sans-serif; font-weight: 600; font-size: 44px; color: var(--accent-red); line-height: 1; }
  .accent-fr { top: 316px; }
  .scent { font-weight: 700; font-size: 24px; letter-spacing: 0.5px; color: var(--soft-grey); line-height: 1; }
  .scent-fr { top: 377px; }

  .free-list { position: absolute; left: 240px; display: flex; align-items: center; }
  .free-list .zero { font-weight: 700; font-size: 42px; width: 62px; color: var(--text-grey); }
  .free-list ul {
    list-style: none; border-left: 1.5px solid var(--accent-red);
    padding-left: 11px; font-size: 20.5px; line-height: 21.5px; color: var(--soft-grey);
  }
  .free-fr { top: 418px; }
  .free-en { top: 675px; }

  .accent-en { top: 548px; }
  .title-en { top: 596px; }
  .scent-en { top: 640px; }

  .vegan-badge { position: absolute; left: 361px; top: 808px; width: 144px; height: 144px; }

  .volume-band {
    position: absolute; left: 0; top: 982px; width: 100%; height: 72px;
    background: var(--red); color: var(--white);
    font-weight: 500; font-size: 56px; line-height: 72px; text-align: center;
  }
</style>
</head>
<body>
  <main class="label">
    <div class="leaf-backdrop" role="img" aria-label="Faint grey leaf branches in the background"></div>

    <div class="centered brand">VERA-MOLUND</div>
    <div class="brand-rule"></div>

    <svg class="paw-icon" viewBox="0 0 110 110" aria-label="Dog paw icon" role="img">
      <circle cx="55" cy="55" r="50" fill="#fff" stroke="#4a4a4a" stroke-width="6"/>
      <ellipse cx="45" cy="36" rx="7" ry="9" fill="var(--red)"/>
      <ellipse cx="65" cy="36" rx="7" ry="9" fill="var(--red)"/>
      <ellipse cx="31" cy="51" rx="6" ry="8" fill="var(--red)"/>
      <ellipse cx="79" cy="51" rx="6" ry="8" fill="var(--red)"/>
      <path d="M55 50 C44 50 33 66 35 74 C37 80 46 78 55 76 C64 78 73 80 75 74 C77 66 66 50 55 50 Z" fill="var(--red)"/>
    </svg>

    <div class="centered title-fr">SHAMPOOING</div>
    <div class="centered title-accent accent-fr">DOUX</div>
    <div class="centered scent scent-fr">MIEL ET ORANGE DOUCE</div>

    <div class="free-list free-fr">
      <span class="zero">0%</span>
      <ul>
        <li>Produits issus de la pétro-chimie</li>
        <li>Paraben</li>
        <li>Colorant</li>
        <li>Parfum synthétique</li>
        <li>Silicone</li>
      </ul>
    </div>

    <div class="centered title-accent accent-en">MILD</div>
    <div class="centered title-fr title-en">SHAMPOO</div>
    <div class="centered scent scent-en">HONEY AND SWEET ORANGE</div>

    <div class="free-list free-en">
      <span class="zero">0%</span>
      <ul>
        <li>petro-chemical products</li>
        <li>Paraben</li>
        <li>Dye</li>
        <li>Synthetic fragrance</li>
        <li>Silicone</li>
      </ul>
    </div>

    <svg class="vegan-badge" viewBox="0 0 144 144" role="img" aria-label="Plant-based badge">
      <circle cx="72" cy="72" r="72" fill="var(--green)"/>
      <circle cx="72" cy="72" r="36" fill="#fff"/>
    </svg>

    <div class="volume-band">200 ml</div>
  </main>
</body>
</html>
```